Infographic for B2B Service solution offering (sales funnel)

Attached is an example of something we need assistance with making into a more professional infographic. These infographics are for our B2B marketing services, aimed at IT Consulting firms.

We have done some basic graphics (attached) and this will provide you guidance (video link on google sheet):
https://pages.vardolink.net/sheet/r/7kQm3TzP9wLcYe2HbNvAsDxR4uFgJ8tWoZiE6yKpBq/view?mode=shared

Here are some examples you can model for the new infographic:
https://vault.vardolink.net/store/groups/48PkTwMz3nRq9LbXvYc-hsd2FjQe?ref=store_link

Target Market(s)

B2B IT Consulting Firms

Industry/Entity Type

Information Technology, Consulting

Colors

Designer to choose colors to be used in the design.

Requirements
Must have
• professional, high level consulting firms are target market
Should not have
• cartoonish

```html
<!DOCTYPE html>
<html lang="en">
<head>
<meta charset="utf-8">
<title>Creating B2B Relationships – Trust Building Offers Method</title>
<link rel="stylesheet" href="https://fonts.googleapis.com/css2?family=Montserrat:wght@600;700;800;900&display=swap">
<style>
  :root {
    --bg: #f2f2f0;
    --ink: #000000;
    --white: #ffffff;
    --stage-a: #eb6532;
    --stage-b: #f6a81b;
    --stage-c: #84bd41;
    --stage-d: #19b4a8;
    --stage-e: #4175bb;
    --stage-f: #64598f;
    --stage-g: #9e4380;
    --trust-low: #d94848;
    --trust-mid: #f4e31c;
    --trust-high: #86be43;
  }
  html, body {
    margin: 0;
    padding: 0;
    width: 1200px;
    height: 1200px;
    overflow: hidden;
    background: var(--bg);
  }
  .infographic {
    display: block;
    width: 1200px;
    height: 1200px;
    font-family: "Montserrat", sans-serif;
  }
  .title-banner { fill: var(--ink); }
  .title-text {
    fill: var(--white);
    font-weight: 600;
    font-size: 36px;
    text-anchor: middle;
  }
  .section-heading {
    fill: var(--ink);
    font-weight: 800;
    font-size: 44px;
    text-anchor: middle;
  }
  .funnel-entry {
    fill: var(--ink);
    font-weight: 900;
    font-size: 34px;
    text-anchor: middle;
  }
  .connector { stroke: var(--ink); stroke-width: 2; fill: none; }
  .dot { fill: var(--ink); }
  .funnel-outline { fill: none; stroke: var(--ink); stroke-width: 2; stroke-linejoin: miter; }
  .band-a { fill: var(--stage-a); }
  .band-b { fill: var(--stage-b); }
  .band-c { fill: var(--stage-c); }
  .band-d { fill: var(--stage-d); }
  .band-e { fill: var(--stage-e); }
  .band-f { fill: var(--stage-f); }
  .band-g { fill: var(--stage-g); }
  .stage-badge-letter {
    fill: var(--white);
    font-weight: 900;
    font-size: 56px;
    text-anchor: middle;
    dominant-baseline: central;
  }
  .stage-name { fill: var(--ink); font-weight: 900; font-size: 29px; }
  .stage-offer { fill: var(--ink); font-weight: 800; font-size: 14px; }
  .stage-risk { fill: var(--ink); font-weight: 700; font-size: 14px; letter-spacing: 0.2px; }
  .trust-label { font-weight: 700; font-size: 29px; text-anchor: middle; }
  .trust-label-low { fill: var(--trust-low); }
  .trust-label-high { fill: var(--trust-high); }
</style>
</head>
<body>
<svg class="infographic" viewBox="0 0 1200 1200" xmlns="http://www.w3.org/2000/svg">
  <defs>
    <filter id="funnel-shadow" x="-20%" y="-10%" width="140%" height="130%">
      <feDropShadow dx="8" dy="6" stdDeviation="5" flood-color="#5a6270" flood-opacity="0.35"/>
    </filter>
    <linearGradient id="trust-gradient" x1="0" y1="432" x2="0" y2="1028" gradientUnits="userSpaceOnUse">
      <stop offset="0" stop-color="#d94848"/>
      <stop offset="0.5" stop-color="#e07a45"/>
      <stop offset="0.65" stop-color="#f4e31c"/>
      <stop offset="0.8" stop-color="#86be43"/>
      <stop offset="1" stop-color="#86be43"/>
    </linearGradient>
  </defs>

  <!-- Title banner -->
  <path class="title-banner" d="M155 177.6 V69.5 Q155 38.5 186 38.5 H1019 Q1050 38.5 1050 69.5 V177.6 Z"/>
  <text class="title-text" x="602" y="90">Creating B2B Relationships:</text>
  <text class="title-text" x="602" y="138">The Corvanth IT “Trust Building Offers” Method</text>

  <text class="section-heading" x="604" y="258">HOW RELATIONSHIPS ARE BUILT</text>
  <text class="funnel-entry" x="602" y="321">COLD LEADS</text>

  <!-- Entry connector -->
  <line class="connector" x1="602" y1="338" x2="602" y2="376"/>
  <circle class="dot" cx="602" cy="338" r="7"/>
  <circle class="dot" cx="602" cy="376" r="7"/>

  <!-- Funnel -->
  <g class="funnel" filter="url(#funnel-shadow)">
    <polygon class="band-a" points="331,390 876,390 794.6,520 412.8,520"/>
    <polygon class="band-b" points="412.8,520 794.6,520 730.6,622 477,622"/>
    <polygon class="band-c" points="477,622 730.6,622 668,722 540,722"/>
    <polygon class="band-d" points="540,722 668,722 655,742 655,822 551,822 551,742"/>
    <rect class="band-e" x="551" y="822" width="104" height="103"/>
    <rect class="band-f" x="551" y="925" width="104" height="102"/>
    <polygon class="band-g" points="551,1027 655,1027 655,1130 551,1053"/>
  </g>
  <path class="funnel-outline" d="M331 390 H876 L668 722 L655 742 V1130 L551 1053 V742 L540 722 Z"/>

  <!-- Band separators -->
  <g class="connector">
    <line x1="374" y1="520" x2="830" y2="520"/>
    <line x1="430" y1="622" x2="775" y2="622"/>
    <line x1="504" y1="722" x2="701" y2="722"/>
    <line x1="534" y1="822" x2="671" y2="822"/>
    <line x1="534" y1="925" x2="671" y2="925"/>
    <line x1="534" y1="1027" x2="671" y2="1027"/>
  </g>

  <!-- Stages -->
  <g class="stage">
    <circle class="band-a" cx="71.5" cy="475" r="40"/>
    <text class="stage-badge-letter" x="71.5" y="477">A</text>
    <line class="connector" x1="112" y1="475" x2="470" y2="475"/>
    <circle class="dot" cx="470" cy="475" r="7.5"/>
    <text class="stage-name" x="123" y="467">PHONE #</text>
    <text class="stage-offer" x="124" y="492">OFFER #1</text>
    <text class="stage-risk" x="124" y="512">LOW RISK, LOW INVESTMENT</text>
  </g>
  <g class="stage">
    <circle class="band-b" cx="71.5" cy="571" r="40"/>
    <text class="stage-badge-letter" x="71.5" y="573">B</text>
    <line class="connector" x1="112" y1="571" x2="515" y2="571"/>
    <circle class="dot" cx="515" cy="571" r="7.5"/>
    <text class="stage-name" x="123" y="563">COFFEE</text>
    <text class="stage-offer" x="124" y="588">OFFER #2</text>
    <text class="stage-risk" x="124" y="608">LOW RISK, MEDIUM INVESTMENT</text>
  </g>
  <g class="stage">
    <circle class="band-c" cx="71.5" cy="673" r="40"/>
    <text class="stage-badge-letter" x="71.5" y="675">C</text>
    <line class="connector" x1="112" y1="673" x2="561" y2="673"/>
    <circle class="dot" cx="561" cy="673" r="7.5"/>
    <text class="stage-name" x="123" y="665">DINNER</text>
    <text class="stage-offer" x="124" y="690">OFFER #3</text>
    <text class="stage-risk" x="124" y="710">MEDIUM RISK, MEDIUM INVESTMENT</text>
  </g>
  <g class="stage">
    <circle class="band-d" cx="71.5" cy="774" r="40"/>
    <text class="stage-badge-letter" x="71.5" y="776">D</text>
    <line class="connector" x1="112" y1="774" x2="603" y2="774"/>
    <circle class="dot" cx="603" cy="774" r="7.5"/>
    <text class="stage-name" x="123" y="766">WEEKEND TRAVEL</text>
    <text class="stage-offer" x="124" y="791">OFFER #4</text>
    <text class="stage-risk" x="124" y="811">HIGH RISK, MEDIUM INVESTMENT</text>
  </g>
  <g class="stage">
    <circle class="band-e" cx="71.5" cy="873" r="40"/>
    <text class="stage-badge-letter" x="71.5" y="875">E</text>
    <line class="connector" x1="112" y1="873" x2="602" y2="873"/>
    <circle class="dot" cx="602" cy="873" r="7.5"/>
    <text class="stage-name" x="123" y="865">MEET PARENTS</text>
    <text class="stage-offer" x="124" y="890">OFFER #5</text>
    <text class="stage-risk" x="124" y="910">MEDIUM RISK, HIGH INVESTMENT</text>
  </g>
  <g class="stage">
    <circle class="band-f" cx="71.5" cy="969" r="40"/>
    <text class="stage-badge-letter" x="71.5" y="971">F</text>
    <line class="connector" x1="112" y1="969" x2="602" y2="969"/>
    <circle class="dot" cx="602" cy="969" r="7.5"/>
    <text class="stage-name" x="123" y="961">MOVE IN</text>
    <text class="stage-offer" x="124" y="986">OFFER #6</text>
    <text class="stage-risk" x="124" y="1006">HIGH RISK, HIGH INVESTMENT</text>
  </g>
  <g class="stage">
    <circle class="band-g" cx="71.5" cy="1066" r="40"/>
    <text class="stage-badge-letter" x="71.5" y="1068">G</text>
    <line class="connector" x1="112" y1="1066" x2="601" y2="1066"/>
    <circle class="dot" cx="601" cy="1063" r="7.5"/>
    <text class="stage-name" x="123" y="1058">WIFE</text>
    <text class="stage-offer" x="124" y="1083">OFFER #7</text>
    <text class="stage-risk" x="124" y="1103">HIGH RISK, HIGH INVESTMENT</text>
  </g>

  <!-- Trust scale -->
  <g class="trust-scale">
    <text class="trust-label trust-label-low" x="1029" y="415">Low Trust</text>
    <rect x="1027" y="432" width="4" height="596" fill="url(#trust-gradient)"/>
    <circle cx="1029" cy="432" r="7" fill="var(--trust-low)"/>
    <circle cx="1029" cy="1028" r="7" fill="var(--trust-high)"/>
    <text class="trust-label trust-label-high" x="1029" y="1068">High Trust</text>
  </g>
</svg>
</body>
</html>
```